Cover-Design für Buch über das Vater-Werden
Das Design hat genau die Beschreibung meines Briefings getroffen und mich sofort überzeugt. Die Idee war klasse.
Zielgruppe
Ich bin vor einem Jahr Vater geworden und habe spontan ein Buch über das Vater-Werden geschrieben. Die Zielgruppe sind also werdende Väter.
Aufgabenstellung
'Zwischen Wiege und Werkbank' ist ein smarter Ratgeber für werdende Väter. Er ist durchaus ernst gemeint, informativ und liefert Fakten. Aber er ist mit einem Augenzwinkern geschrieben und mit amüsanten Anekdoten untermalt, so dass der Ratgeber kurzweilig zu lessen ist. Das Buch behandelt die Zeitspanne vom Beginn bis zum Ende der Schwangerschaft. Zum besseren inhaltlichen Verständnis habe ich ein Exposé angehängt.

```html
<!DOCTYPE html>
<html lang="de">
<head>
<meta charset="utf-8">
<title>Zwischen Wiege und Werkbank – Buchcover</title>
<link rel="stylesheet" href="https://fonts.googleapis.com/css2?family=Michroma&family=Oxanium:wght@700&display=swap">
<style>
  :root {
    --backdrop: #c5df8a;
    --cover-blue: #3fb3e3;
    --title-lime: #c8e08d;
    --tagline-navy: #1f2f6b;
    --art-deep: #2a62b0;
    --art-light: #eef6fb;
  }
  html, body {
    margin: 0;
    padding: 0;
    width: 1200px;
    height: 1200px;
    overflow: hidden;
    background: var(--backdrop);
  }
  .canvas {
    position: relative;
    width: 1200px;
    height: 1200px;
    background: var(--backdrop);
  }
  .book-cover {
    position: absolute;
    left: 271px;
    top: 106px;
    width: 657px;
    height: 987px;
    background: var(--cover-blue);
    text-align: center;
    overflow: hidden;
  }
  .tagline {
    position: absolute;
    top: 20px;
    left: 0;
    right: 0;
    margin: 0;
    font-family: "Oxanium", sans-serif;
    font-weight: 700;
    font-size: 25px;
    line-height: 28px;
    letter-spacing: 0.42em;
    color: var(--tagline-navy);
    text-transform: uppercase;
    padding-left: 0.42em;
  }
  .title {
    position: absolute;
    top: 128px;
    left: 0;
    right: 0;
    margin: 0;
    font-family: "Michroma", sans-serif;
    font-weight: 400;
    color: var(--title-lime);
    text-transform: uppercase;
  }
  .title-line {
    display: block;
    white-space: nowrap;
  }
  .title-line--small {
    font-size: 60px;
    line-height: 102px;
  }
  .title-line--large {
    font-size: 74px;
    line-height: 150px;
  }
  .cover-art {
    position: absolute;
    left: 201px;
    top: 546px;
    width: 277px;
    height: 336px;
    border-radius: 48% 48% 42% 42% / 38% 38% 30% 30%;
    background: radial-gradient(ellipse at 55% 65%, var(--art-light) 0%, var(--art-light) 34%, var(--art-deep) 62%, #1e4f98 100%);
  }
  .author {
    position: absolute;
    top: 908px;
    left: 0;
    right: 0;
    margin: 0;
    font-family: "Oxanium", sans-serif;
    font-weight: 700;
    font-size: 40px;
    letter-spacing: 0.32em;
    padding-left: 0.32em;
    color: var(--title-lime);
    text-transform: uppercase;
  }
</style>
</head>
<body>
  <main class="canvas">
    <article class="book-cover">
      <p class="tagline">Der smarte Ratgeber für<br>werdende Väter</p>
      <h1 class="title">
        <span class="title-line title-line--small">Zwischen</span>
        <span class="title-line title-line--small">Wiege und</span>
        <span class="title-line title-line--large">Werkbank</span>
      </h1>
      <div class="cover-art" role="img" aria-label="Aquarell-Illustration eines blau-weißen Pinguins, der ein Ei vor seinem Bauch hält"></div>
      <p class="author">Tobias Kelsch</p>
    </article>
  </main>
</body>
</html>
```